サイト構成・基本的な要件については
https://zuvela.com/boards/7kQwLmTn28XpaRzd
をご参照ください。
ただ、レイアウトについては、各コンテンツへの導線が確保されていれば、
上記レイアウト案を必ず守る必要はございません。

写真素材については、
http://hakoyuki.jp/fetch/8b1d2f7a4c6e90135d7a8b2c4e6f1a3b5d7c9e0a
よりダウンロードください。
また、こちらだけですと作成が難しいと思いますので。。
http://gorumo.jp/
などから、10000円程度までならこちらにて購入可能です。

ロゴについては、
添付のデータを展開していただく形でご利用ください。

丸太のマークをご利用いただければ、
その他の要素(Wood Working Shop / 浅沼工房の丸太文字)については
必ずしも使用しなくてかまいません。
位置の変更も問題ございません。

【参考サイト】
http://www.surinavel.com/
http://kabuteya.jp/

白ベースの配色で、
少し木の温かみを感じるようなデザインを希望いたします。

基本レイアウト
については、必ずしも忠実である必要はありません。
特に今後大きく構成が変わる予定はございませんので、
各コンテンツへの導線を確保してあれば
必ずしも上記に準じている必要はありません。
ご自由にご提案いただいても結構です。
2カラムのご提案でも問題ございません。
また、当方jqueryを使用したコーディングも可能です。

恐れ入りますが、何卒よろしくお願いいたします。
http://www.lumio-t.hinoka.ne.jp/
茶系
【素材データについて】
よりダウンロードください。
http://gorumo.jp/
カンプデータにて作成頂き、納品時に当方にて購入したデータに差し替えていただければと存じます。

【参考サイト】
http://www.surinavel.com/
http://kabuteya.jp/

落ち着きがあり、信頼性を感じるデザインを希望いたします。
トップページで、いくつかの施工写真を見せられればと思います。
あまり無機質になりすぎず、木の温かみを感じるようなイメージですと
大変ありがたく存じます。

http://pagebase-lab.com/2012/166.html
http://pagebase-lab.com/2011/115.html
→フッター部分の参考です

ご提案に関しまして、不明点等ございましたらお気軽にお申し付けください。

クライアントとの協議の結果、こちらの案を採用させていただきました。
サイト全体の見やすさ、信頼感、清潔感
文字などの読みやすさが大変気に入り、
そちらが採用の決め手となりました。

この度は多数ご提案いただきありがとうございました。
当選に至らなかったランサー様におかれましては大変心苦しいのですが、
次の機会にぜひご提案いただければ幸甚です。
引き続き何卒よろしくお願いいたします。

```html
<!DOCTYPE html>
<html lang="ja">
<head>
<meta charset="utf-8">
<title>浅沼工房</title>
<link href="https://fonts.googleapis.com/css2?family=Noto+Sans+JP:wght@400;500;700&family=Noto+Serif+JP:wght@500;700&family=Cormorant+Garamond:wght@500&display=swap" rel="stylesheet">
<style>
:root{
  --bg:#ffffff;
  --text:#4a4540;
  --muted:#8a847d;
  --brown:#8b5a2b;
  --accent:#c8a27a;
  --line:#d9d4cd;
  --footer:#eeebe7;
  --hero-a:#cbb89c;
  --hero-b:#efe7da;
}
*{margin:0;padding:0;box-sizing:border-box}
html,body{width:750px;height:1200px;overflow:hidden;background:var(--bg)}
body{font-family:"Noto Sans JP",sans-serif;color:var(--text);position:relative}
.header{position:absolute;left:0;top:0;width:750px;height:78px}
.brand{position:absolute;left:28px;top:20px;display:flex;align-items:center;gap:10px}
.brand-dot{width:30px;height:30px;border-radius:50%;background:var(--brown)}
.brand-name{font-family:"Noto Serif JP",serif;font-weight:700;font-size:22px;color:var(--text);letter-spacing:2px}
.contact{position:absolute;left:480px;top:8px;font-size:11px;line-height:15px}
.contact .lead{color:var(--brown);font-weight:500}
.contact .tel{font-size:12px}
.contact .hours{font-size:8px;color:var(--muted)}
.contact-btn{position:absolute;left:620px;top:30px;width:110px;height:20px;border-radius:10px;background:var(--accent);color:#fff;font-size:10px;text-align:center;line-height:20px}
.hero{position:absolute;left:0;top:78px;width:750px;height:300px;background:linear-gradient(90deg,var(--hero-a),var(--hero-b) 55%,var(--hero-a))}
.hero-copy{position:absolute;right:70px;top:155px;text-align:center;color:#fff;font-family:"Noto Serif JP",serif;font-weight:700}
.hero-copy span{display:inline-block;background:rgba(60,45,30,.55);padding:2px 10px;margin-bottom:6px}
.hero-copy .year{font-size:20px}
.hero-copy .tag{font-size:18px}
.nav{position:absolute;left:65px;top:393px;display:flex;gap:26px;font-size:12px}
.nav a{color:var(--text);text-decoration:none;padding-bottom:5px}
.nav a.active{border-bottom:2px solid var(--brown)}
.nav-rule{position:absolute;left:65px;top:415px;width:620px;border-top:1px solid var(--line)}
.section-title{position:absolute;left:0;width:750px;text-align:center;font-family:"Cormorant Garamond",serif;font-size:34px;letter-spacing:3px;color:var(--text)}
.works-lead{position:absolute;left:0;top:505px;width:750px;text-align:center;font-size:10px;line-height:17px;color:var(--muted)}
.works-grid{position:absolute;left:20px;top:560px;width:710px;height:165px;display:flex;gap:6px}
.works-grid div{flex:1}
.w1{background:linear-gradient(#d9cbb5,#b99a74)}
.w2{background:linear-gradient(#eae5dc,#c7b393)}
.w3{background:linear-gradient(#d3b88f,#a98458)}
.w4{background:linear-gradient(#f0e6d6,#c29a68)}
.news-list{position:absolute;left:110px;top:868px;width:540px;list-style:none;font-size:12px;line-height:22px}
.news-list time{color:var(--muted);margin-right:12px}
.more{position:absolute;left:610px;top:942px;font-size:11px;color:var(--text)}
.footer{position:absolute;left:0;top:1010px;width:750px;height:150px;background:var(--footer)}
.footer .brand{left:35px;top:18px}
.footer .brand-dot{width:24px;height:24px}
.footer .brand-name{font-size:18px}
.footer-info{position:absolute;left:35px;top:60px;font-size:9px;line-height:14px;color:var(--muted)}
.footer-nav{position:absolute;top:18px;list-style:none;font-size:11px;line-height:17px}
.footer-nav li::before{content:"›";color:var(--brown);margin-right:5px}
.fn1{left:325px}.fn2{left:510px}
.copyright{position:absolute;left:0;top:1170px;width:750px;text-align:center;font-size:8px;color:var(--muted)}
</style>
</head>
<body>
<header class="header">
  <div class="brand"><span class="brand-dot"></span><span class="brand-name">浅沼工房</span></div>
  <div class="contact">
    <div class="lead">お気軽にお問い合わせください!</div>
    <div class="tel">Tel 0120-48-3615</div>
    <div class="tel">Fax 0120-48-3616</div>
    <div class="hours">受付時間 8:00〜17:30（日・祝休み）</div>
  </div>
  <div class="contact-btn">お問い合わせフォーム</div>
</header>

<section class="hero" role="img" aria-label="明るい和室に並ぶ木製の格子戸と障子">
  <div class="hero-copy">
    <span class="year">創業大正二年</span><br>
    <span class="tag">木製建具・家具のことならお任せください</span>
  </div>
</section>

<nav class="nav">
  <a class="active">トップページ</a><a>営業品目</a><a>施工例</a><a>お取引の流れ</a><a>よくあるご質問</a><a>会社概要</a>
</nav>
<div class="nav-rule"></div>

<h2 class="section-title" style="top:455px">WORKS</h2>
<p class="works-lead">和建具の製作・取り付けから、一般住宅の室内ドア・窓の製作<br>収納家具・トイレブースなど幅広く製作しております。</p>
<div class="works-grid">
  <div class="w1" role="img" aria-label="造り付けの木製収納棚"></div>
  <div class="w2" role="img" aria-label="白い室内ドアのある廊下"></div>
  <div class="w3" role="img" aria-label="格子の木製玄関引き戸"></div>
  <div class="w4" role="img" aria-label="アーチ窓のある木の室内"></div>
</div>

<h2 class="section-title" style="top:815px">NEWS</h2>
<ul class="news-list">
  <li><time>2017.07.01</time>新着情報タイトル新着情報タイトル新着情報タイトル新着情報タイトル</li>
  <li><time>2017.07.01</time>新着情報タイトル新着情報タイトル</li>
  <li><time>2017.07.01</time>新着情報タイトル新着情報タイトル新着情報タイトル</li>
</ul>
<div class="more">› すべて見る</div>

<footer class="footer">
  <div class="brand"><span class="brand-dot"></span><span class="brand-name">浅沼工房</span></div>
  <div class="footer-info">
    神奈川県架空市桜台 2-14<br>
    Tel 0120-48-3615 / FAX 0120-48-3616<br>
    営業時間：8:00〜17:30（日・祝）
  </div>
  <ul class="footer-nav fn1">
    <li>トップページ</li><li>営業品目</li><li>施工例</li><li>お取引の流れ</li><li>よくあるご質問</li><li>会社概要</li>
  </ul>
  <ul class="footer-nav fn2">
    <li>お問い合わせ</li><li>お知らせ</li><li>プライバシーポリシー</li><li>サイトマップ</li>
  </ul>
</footer>
<p class="copyright">Copyright © 2017 浅沼工房 All Rights Reserved.</p>
</body>
</html>
```